Business card design needed

We require a business card and logo design for our tipper truck business which services the building and agricultural industries, based in Albury-Wodonga, Australia. The business name is 'Falcon Haulage' and our business moto is 'if it's tippable, it's doable'.
If a tipper truck is to be included in the logo, the truck must not have a nose ie. the truck must have a flat front.
The moto for the Albury-Wodonga region is 'where the mountains meet the murray' (snowy mountains meet murray river-this may or may not be included in the image design)

Industry/Entity Type

Building

Contact Information for Business Card

FALCON HAULAGE PTY LTD
Complete Dumping Solutions
If it tips, we can move it!
Col Brimble
0483 906 217
falconhaulage@quillmail.com.au
PO Box 829
Fernvale NSW 2739
ABN: 57 309 842 615

```html
<!DOCTYPE html>
<html lang="en">
<head>
<meta charset="utf-8">
<title>Falcon Haulage – Business Card</title>
<link rel="stylesheet" href="https://fonts.googleapis.com/css2?family=Montserrat:wght@300;400;600;700&display=swap">
<style>
  :root {
    --brand-orange: #e44d23;
    --brand-grey: #5a5756;
    --card-white: #ffffff;
    --text-dark: #555352;
  }
  html, body {
    margin: 0;
    padding: 0;
    width: 1200px;
    height: 693px;
    overflow: hidden;
    background: var(--card-white);
  }
  .card {
    position: relative;
    width: 1200px;
    height: 693px;
    background: var(--brand-orange);
    overflow: hidden;
    font-family: "Montserrat", sans-serif;
  }
  .card__wave {
    position: absolute;
    inset: 0;
    width: 1200px;
    height: 693px;
  }
  .brand__mark {
    position: absolute;
    left: 880px;
    top: 108px;
    width: 60px;
    height: 60px;
    background: var(--brand-orange);
  }
  .brand__service {
    position: absolute;
    left: 652px;
    top: 178px;
    margin: 0;
    font-size: 15px;
    font-weight: 400;
    line-height: 1;
    color: var(--brand-orange);
    white-space: nowrap;
  }
  .brand__name {
    position: absolute;
    right: 60px;
    top: 192px;
    margin: 0;
    font-size: 43px;
    font-weight: 600;
    color: var(--text-dark);
    letter-spacing: -0.5px;
    line-height: 1;
    white-space: nowrap;
  }
  .brand__motto {
    position: absolute;
    right: 60px;
    top: 238px;
    margin: 0;
    font-size: 17px;
    font-weight: 300;
    line-height: 1;
    color: var(--text-dark);
    white-space: nowrap;
  }
  .holder-name {
    position: absolute;
    left: 60px;
    top: 249px;
    margin: 0;
    font-size: 84px;
    font-weight: 700;
    color: var(--card-white);
    line-height: 1;
    white-space: nowrap;
  }
  .contact {
    position: absolute;
    left: 58px;
    top: 450px;
    margin: 0;
    padding: 0;
    list-style: none;
    color: var(--card-white);
    font-size: 32px;
    font-weight: 300;
  }
  .contact__item {
    display: flex;
    align-items: flex-start;
    gap: 22px;
    line-height: 42px;
    white-space: nowrap;
  }
  .contact__item--phone { margin-bottom: 18px; }
  .contact__item--email { margin-bottom: 8px; }
  .contact__icon {
    flex: 0 0 30px;
    width: 30px;
    height: 42px;
  }
</style>
</head>
<body>
  <main class="card">
    <svg class="card__wave" viewBox="0 0 1200 693" aria-hidden="true">
      <path fill="var(--brand-grey)" d="M780 0 C590 55 490 125 525 205 C555 300 715 345 840 450 C905 520 880 610 790 693 L1200 693 L1200 0 Z"/>
      <path fill="var(--card-white)" d="M796 0 C600 50 500 120 531 200 C560 290 720 330 850 440 C920 510 900 600 810 693 L1200 693 L1200 0 Z"/>
    </svg>

    <header class="brand">
      <span class="brand__mark" aria-hidden="true"></span>
      <p class="brand__service">Complete Dumping Solutions</p>
      <h2 class="brand__name">Falcon Haulage PTY LTD</h2>
      <p class="brand__motto">If it tips, we can move it!</p>
    </header>

    <h1 class="holder-name">Col Brimble</h1>

    <ul class="contact">
      <li class="contact__item contact__item--phone">
        <svg class="contact__icon" viewBox="0 0 30 42" aria-hidden="true">
          <path fill="var(--card-white)" d="M9 8 L14 7 L16 16 L12 18 C13 23 15 27 18 30 L21 27 L27 33 L23 37 C13 36 5 22 9 8 Z"/>
        </svg>
        <span>0483 906 217</span>
      </li>
      <li class="contact__item contact__item--email">
        <svg class="contact__icon" viewBox="0 0 30 42" aria-hidden="true">
          <rect x="2" y="12" width="26" height="18" fill="none" stroke="var(--card-white)" stroke-width="2.5"/>
          <path d="M2 12 L15 23 L28 12 M2 30 L11 20 M28 30 L19 20" fill="none" stroke="var(--card-white)" stroke-width="2.5"/>
        </svg>
        <span>falconhaulage@quillmail.com.au</span>
      </li>
      <li class="contact__item contact__item--address">
        <svg class="contact__icon" viewBox="0 0 30 42" aria-hidden="true">
          <g fill="none" stroke="var(--card-white)" stroke-width="2">
            <circle cx="15" cy="21" r="12"/>
            <ellipse cx="15" cy="21" rx="5" ry="12"/>
            <path d="M3 21 H27 M5 14 H25 M5 28 H25"/>
          </g>
        </svg>
        <span>PO Box 829 Fernvale NSW 2739<br>ABN: 57 309 842 615</span>
      </li>
    </ul>
  </main>
</body>
</html>
```